we are an outdoor outlet in a country club that has a variety of outlets. The Club is called Fernwold and is located in Cairo, Egypt. This garden menu will include cuisines from the Mediterranean, Asia and Texmex. we need a menu that is colorful and would fit an A3 size, back and front are to be used. Attached is the old menu currently in use (Garden Menu 2012.pdf is just for reference) and the new menu text for you to use is under the name Garden Menu Fall 2013
thank you.

```html
<!DOCTYPE html>
<html lang="en">
<head>
<meta charset="utf-8">
<title>Fernwold Garden Menu</title>
<link href="https://fonts.googleapis.com/css2?family=Josefin+Sans:wght@300;400;600;700&family=Roboto+Slab:wght@400;700&display=swap" rel="stylesheet">
<style>
  :root {
    --panel-dark: #cf4f1b;
    --panel-mid: #f7982a;
    --ribbon: #a3261e;
    --ribbon-fold: #7c1a14;
    --badge: #9a2a22;
    --text-light: #ffffff;
    --text-dark: #3a1a0c;
    --desc-yellow: #f8e071;
    --rule-light: #f6c9a6;
  }
  * { margin: 0; padding: 0; box-sizing: border-box; }
  html, body { width: 1200px; height: 848px; overflow: hidden; background: #ffffff; }
  .menu { width: 1200px; height: 848px; position: relative; overflow: hidden; }
  .sheet {
    width: 1190px; height: 841px; position: absolute; left: 0; top: 0;
    transform: scale(1.0084, 1.0083); transform-origin: 0 0;
    font-family: "Josefin Sans", sans-serif;
  }
  .panel { position: absolute; top: 0; height: 841px; }
  .panel-left { left: 0; width: 397px; background: var(--panel-dark); color: var(--text-light); }
  .panel-middle { left: 397px; width: 396px; background: var(--panel-mid); color: var(--text-dark); }
  .panel-right { left: 793px; width: 397px; background: var(--panel-dark); color: var(--text-light); }

  .brand-title { position: absolute; left: 48px; top: 32px; display: flex; align-items: center; gap: 10px;
    font-weight: 300; font-size: 40px; letter-spacing: 0.5px; }
  .brand-dot { width: 30px; height: 30px; border-radius: 50%; background: var(--text-light); }

  .food-photo { position: absolute; left: 0; top: 93px; width: 397px; height: 172px;
    background: linear-gradient(120deg, #7b5a3a 0%, #a8703c 30%, #c9a36a 55%, #d7b98a 75%, #8f9a48 100%); }
  .pizza-photo { position: absolute; left: 67px; top: 742px; width: 272px; height: 200px; border-radius: 50%;
    background: radial-gradient(circle at 50% 40%, #f2e6c8 0%, #d9a25b 45%, #b8562a 70%, #c98b4a 100%); }

  .ribbon { position: absolute; left: 0; top: 222px; width: 297px; height: 54px; }
  .ribbon-band { position: absolute; left: 0; top: 0; width: 297px; height: 54px; background: var(--ribbon); }
  .ribbon-text { position: absolute; left: 55px; top: 3px; font-size: 26px; line-height: 26px; font-weight: 300; color: var(--text-light); }
  .ribbon-folds { position: absolute; left: 0; top: 0; }

  .section-title { position: absolute; text-align: center; font-weight: 700; letter-spacing: 4px; }
  .panel-left .section-title, .panel-right .section-title { color: var(--text-light); font-size: 23px; }
  .panel-middle .section-title { color: var(--text-dark); font-size: 19px; }
  .section-note { position: absolute; text-align: center; font-family: "Roboto Slab", serif; font-size: 9.5px; }

  .divider { position: absolute; height: 20px; }
  .divider-line { position: absolute; left: 0; right: 0; top: 9px; height: 1px; }
  .divider-dot { position: absolute; left: 50%; top: 0; width: 20px; height: 20px; margin-left: -10px; border-radius: 50%; background: var(--text-light); }
  .panel-left .divider-line, .panel-right .divider-line { background: var(--rule-light); }
  .panel-middle .divider-line { background: var(--text-light); }

  .item { position: absolute; }
  .item-head { display: flex; justify-content: space-between; text-transform: uppercase; font-weight: 300; }
  .item-desc { font-family: "Roboto Slab", serif; }
  .panel-left .item-head { font-size: 15px; }
  .panel-left .item-desc { font-size: 11px; line-height: 15.5px; color: var(--desc-yellow); margin-top: 3px; }
  .panel-middle .item-head, .panel-right .item-head { font-size: 12.5px; }
  .panel-middle .item-desc, .panel-right .item-desc { font-size: 9.5px; line-height: 12.5px; margin-top: 1px; }
  .item-head .note { text-transform: none; font-size: 9.5px; font-family: "Roboto Slab", serif; }

  .choices { font-family: "Roboto Slab", serif; font-size: 9.5px; display: flex; flex-wrap: wrap; gap: 3px 4px; }
  .panel-left .choices { font-size: 11px; flex-direction: column; color: var(--desc-yellow); gap: 2px; }
  .choice { display: inline-flex; align-items: center; gap: 2px; }
  .box { display: inline-block; width: 10px; height: 10px; border: 1px solid currentColor; background: rgba(255,255,255,0.15); }
  .choice-label { display: inline-block; width: 44px; font-family: "Roboto Slab", serif; font-size: 9.5px; }

  .club-name { position: absolute; left: 46px; top: 34px; display: flex; align-items: center; gap: 8px; }
  .club-dot { width: 42px; height: 42px; border-radius: 50%; background: var(--text-light); }
  .club-words { line-height: 1; }
  .club-words .main { font-size: 33px; font-weight: 300; display: block; }
  .club-words .sub { font-size: 10px; font-weight: 300; letter-spacing: 4.6px; display: block; margin-top: 2px; }

  .price-badge { position: absolute; left: 266px; top: 15px; width: 96px; height: 96px; border-radius: 50%;
    background: var(--badge); display: flex; align-items: center; justify-content: center; }
  .price-badge-ring { position: absolute; inset: 6px; border: 1.5px solid var(--text-light); border-radius: 50%; }
  .price-badge-text { font-family: "Roboto Slab", serif; font-size: 8px; line-height: 9.5px; text-align: center; text-transform: uppercase; font-weight: 700; }
</style>
</head>
<body>
<div class="menu">
  <div class="sheet">

    <section class="panel panel-left">
      <div class="brand-title"><span class="brand-dot"></span><span>garden menu</span></div>
      <div class="food-photo" role="img" aria-label="Photo of grilled chicken with peppers and olives over couscous"></div>
      <div class="ribbon">
        <div class="ribbon-band"></div>
        <svg class="ribbon-folds" width="297" height="90" viewBox="0 0 297 90">
          <polygon points="0,54 28,54 28,88" fill="var(--ribbon-fold)"/>
          <polygon points="270,54 297,54 270,62" fill="var(--ribbon-fold)"/>
        </svg>
        <div class="ribbon-text">MEDITERRANEAN<br>CORNER</div>
      </div>

      <h2 class="section-title" style="left:0;width:397px;top:288px;">main courses</h2>
      <div class="divider" style="left:56px;width:284px;top:317px;"><span class="divider-line"></span><span class="divider-dot"></span></div>

      <div class="item" style="left:57px;width:283px;top:347px;">
        <div class="item-head"><span>Veal Parmeggiana</span><span>00.00</span></div>
        <p class="item-desc">Breaded veal escalope topped with<br>melted cheese and tomato sauce<br>served with Spaghetti</p>
      </div>
      <div class="item" style="left:57px;width:283px;top:429px;">
        <div class="item-head"><span>Chicken a la Francaise</span><span>00.00</span></div>
        <p class="item-desc">Pan fried chicken breast in a mushroom<br>cream sauce with vegetables white rice</p>
      </div>
      <div class="item" style="left:57px;width:283px;top:495px;">
        <div class="item-head"><span>Grilled Salmon</span><span>00.00</span></div>
        <p class="item-desc">Salmon steak charcoal grilled<br>with avocado tomato relish<br>and creamy mushroom risotto</p>
      </div>
      <div class="item" style="left:57px;width:283px;top:577px;">
        <div class="item-head"><span>Moroccan Chicken</span><span>00.00</span></div>
        <p class="item-desc">Chicken cubes simmered with spices<br>and olives served with tomato rice</p>
      </div>
      <div class="item" style="left:57px;width:280px;top:643px;">
        <div class="item-head"><span>Filet</span><span>00.00</span></div>
        <p class="item-desc">Tender filet grilled to your liking<br>served with mashed potato<br>and creamed spinach</p>
      </div>
      <div class="item" style="left:57px;width:283px;top:725px;">
        <div class="item-head"><span>Choice of Sauces</span></div>
        <div class="choices" style="margin-top:3px;">
          <span class="choice"><span class="box"></span>Brown Mushroom</span>
          <span class="choice"><span class="box"></span>Green Peppercorn</span>
          <span class="choice"><span class="box"></span>Gorgonzola</span>
        </div>
      </div>
    </section>

    <section class="panel panel-middle">
      <h2 class="section-title" style="left:0;width:396px;top:50px;">soups</h2>
      <div class="divider" style="left:56px;width:284px;top:74px;"><span class="divider-line"></span><span class="divider-dot"></span></div>

      <div class="item" style="left:56px;width:284px;top:93px;">
        <div class="item-head"><span>Tomato Basil</span><span>00.00</span></div>
        <p class="item-desc">Simmered tomato soup finished with<br>fresh basil and cream</p>
      </div>
      <div class="item" style="left:56px;width:284px;top:143px;">
        <div class="item-head"><span>Chicken Cream</span><span>00.00</span></div>
        <p class="item-desc">Chicken broth with roasted chicken cubes,<br>pine nuts, and cream</p>
      </div>
      <div class="item" style="left:56px;width:281px;top:193px;">
        <div class="item-head"><span>Moroccan Harira</span><span>00.00</span></div>
        <p class="item-desc">Vegetable broth with fresh tomato,<br>chickpeas, lentil, cilantro, and diced lamb</p>
      </div>

      <h2 class="section-title" style="left:0;width:396px;top:249px;">appetizers</h2>
      <div class="divider" style="left:56px;width:284px;top:274px;"><span class="divider-line"></span><span class="divider-dot"></span></div>

      <div class="item" style="left:56px;width:281px;top:293px;">
        <div class="item-head"><span>Salmon Tartare</span><span>00.00</span></div>
        <p class="item-desc">Seasoned with lemon juice, garlic,<br>and crushed black pepper</p>
      </div>
      <div class="item" style="left:56px;width:281px;top:344px;">
        <div class="item-head"><span>Roasted Eggplant Rolls</span><span>00.00</span></div>
        <p class="item-desc">With herbed ricotta cheese and pine nuts</p>
      </div>
      <div class="item" style="left:56px;width:281px;top:382px;">
        <div class="item-head"><span>Falafel in Mini Pita</span><span>00.00</span></div>
        <p class="item-desc">Served with tehina and oriental salsa</p>
      </div>
      <div class="item" style="left:56px;width:281px;top:421px;">
        <div class="item-head"><span>Mankousha</span><span>00.00</span></div>
        <p class="item-desc">With thyme and olive oil</p>
      </div>
      <div class="item" style="left:56px;width:281px;top:459px;">
        <div class="item-head"><span>Fried Kobeba</span><span>00.00</span></div>
        <p class="item-desc">With minced meat, spices, and pine nuts</p>
      </div>
      <div class="item" style="left:56px;width:281px;top:498px;">
        <div class="item-head"><span>Fried Calamari a la Romana</span><span>00.00</span></div>
        <p class="item-desc">Served with aioli</p>
      </div>
      <div class="item" style="left:56px;width:281px;top:536px;">
        <div class="item-head"><span>Samboussek</span><span>00.00</span></div>
        <p class="item-desc">With herbed white cheese and mint</p>
      </div>
      <div class="item" style="left:56px;width:281px;top:575px;">
        <div class="item-head"><span>Oriental Sausage Sautéed</span><span>00.00</span></div>
        <p class="item-desc">With garlic and onion</p>
      </div>
      <div class="item" style="left:56px;width:281px;top:613px;">
        <div class="item-head"><span>Mini Vine Leaves</span><span>00.00</span></div>
        <p class="item-desc">With a yoghurt dip</p>
      </div>
      <div class="item" style="left:56px;width:281px;top:652px;">
        <div class="item-head"><span>Fatouch</span><span>00.00</span></div>
        <p class="item-desc">With a pomegranate syrup dressing</p>
      </div>
      <div class="item" style="left:56px;width:284px;top:690px;">
        <div class="item-head"><span>Hummus</span><span>00.00</span></div>
        <p class="item-desc">Seasoned with lemon juice, garlic, and olive oil</p>
      </div>
      <div class="item" style="left:56px;width:284px;top:728px;">
        <div class="item-head"><span>White Cheese</span><span>00.00</span></div>
        <p class="item-desc">With diced tomato, thyme, and olive oil</p>
      </div>
      <div class="item" style="left:56px;width:284px;top:767px;">
        <div class="item-head"><span>Tehina</span><span>00.00</span></div>
        <p class="item-desc">Seasoned with cumin, lemon juice, and garlic</p>
      </div>
    </section>

    <section class="panel panel-right">
      <div class="club-name">
        <span class="club-dot"></span>
        <span class="club-words"><span class="main">fernwold</span><span class="sub">country club</span></span>
      </div>
      <div class="price-badge">
        <span class="price-badge-ring"></span>
        <span class="price-badge-text">Prices are<br>subject to<br>12% service<br>charge &amp;<br>10% sales tax</span>
      </div>

      <h2 class="section-title" style="left:0;width:397px;top:116px;">sandwiches</h2>
      <p class="section-note" style="left:0;width:397px;top:139px;">(Served with french fries or garden salad)</p>
      <div class="divider" style="left:58px;width:285px;top:157px;"><span class="divider-line"></span><span class="divider-dot"></span></div>

      <div class="item" style="left:58px;width:284px;top:186px;">
        <div class="item-head"><span>Beef or Chicken Shawerma</span><span>00.00</span></div>
      </div>
      <div class="item" style="left:58px;width:284px;top:215px;">
        <div class="item-head"><span>Grilled Kofta</span><span>00.00</span></div>
      </div>
      <div class="item" style="left:58px;width:284px;top:244px;">
        <div class="item-head"><span>Greek Lamb Gyro</span><span>00.00</span></div>
        <p class="item-desc">in pita bread with Tzatziki</p>
      </div>
      <div class="item" style="left:58px;width:284px;top:282px;">
        <div class="item-head"><span>Club Sandwich</span><span>00.00</span></div>
        <p class="item-desc">with smoked beef, turkey, egg</p>
      </div>

      <h2 class="section-title" style="left:0;width:397px;top:319px;">salads</h2>
      <div class="divider" style="left:58px;width:285px;top:346px;"><span class="divider-line"></span><span class="divider-dot"></span></div>

      <div class="item" style="left:58px;width:282px;top:365px;">
        <div class="item-head"><span>Caprese</span><span>00.00</span></div>
        <p class="item-desc">Buffalo mozzarella and sliced tomato<br>with a balsamic vinaigrette</p>
      </div>
      <div class="item" style="left:58px;width:282px;top:416px;">
        <div class="item-head"><span>Rocket Apple</span><span>00.00</span></div>
        <p class="item-desc">Rocket leaves with gorgonzola, croutons,<br>and strawberry vinaigrette</p>
      </div>
      <div class="item" style="left:58px;width:282px;top:466px;">
        <div class="item-head"><span>French Riviera Nicoise</span><span>00.00</span></div>
        <p class="item-desc">Lettuce, egg, tomato, tuna, olives, onion,<br>celery, radish, bell pepper in a French vinaigrette</p>
      </div>
      <div class="item" style="left:58px;width:282px;top:516px;">
        <div class="item-head"><span>Folle</span><span>00.00</span></div>
        <p class="item-desc">Mixed greens with crab sticks, mushroom,<br>corn, cherry tomato in a mango vinaigrette</p>
      </div>

      <h2 class="section-title" style="left:0;width:397px;top:565px;">pizza &amp; pasta</h2>
      <div class="divider" style="left:58px;width:285px;top:590px;"><span class="divider-line"></span><span class="divider-dot"></span></div>

      <div class="item" style="left:58px;width:283px;top:613px;">
        <div class="item-head"><span>Pizza Margarita <span class="note">(Choose your toppings)</span></span><span>00.00</span></div>
        <div class="choices" style="margin-top:4px;">
          <span class="choice"><span class="box"></span>Bell Peppers</span>
          <span class="choice"><span class="box"></span>Olives</span>
          <span class="choice"><span class="box"></span>Tomato</span>
          <span class="choice"><span class="box"></span>Onion</span>
          <span class="choice"><span class="box"></span>Mushroom</span>
          <span class="choice"><span class="box"></span>Chicken</span>
          <span class="choice"><span class="box"></span>Tuna</span>
          <span class="choice"><span class="box"></span>Pepperoni</span>
          <span class="choice"><span class="box"></span>Smoked Salmon</span>
          <span class="choice"><span class="box"></span>Shrimps</span>
        </div>
      </div>
      <div class="item" style="left:58px;width:283px;top:673px;">
        <div class="item-head"><span>Create Your Own Pasta</span><span>00.00</span></div>
        <div class="choices" style="margin-top:5px;gap:3px 10px;">
          <span class="choice-label">TYPE</span>
          <span class="choice"><span class="box"></span>Spaghetti</span>
          <span class="choice"><span class="box"></span>Tagliatelle</span>
          <span class="choice"><span class="box"></span>Penne</span>
        </div>
        <div class="choices" style="margin-top:3px;gap:3px 10px;">
          <span class="choice-label" style="width:40px;">SAUCES</span>
          <span class="choice"><span class="box"></span>Napolitana</span>
          <span class="choice"><span class="box"></span>Bolognese</span>
          <span class="choice"><span class="box"></span>Alfredo</span>
        </div>
      </div>
      <div class="item" style="left:58px;width:283px;top:733px;">
        <div class="item-head"><span>Lasagna</span><span>00.00</span></div>
      </div>

      <div class="pizza-photo" role="img" aria-label="Photo of a margherita pizza with basil leaves"></div>
    </section>

  </div>
</div>
</body>
</html>
```